showcase project portfolio

create power point of project portfolio
from word file and website using similar design template

https://www.brelvon.co.uk/

Target Market(s)

corporte

```html
<!DOCTYPE html>
<html lang="en">
<head>
<meta charset="utf-8">
<title>Brelvon Innovative Design Solution – Project Portfolio</title>
<link rel="stylesheet" href="https://fonts.googleapis.com/css2?family=Nunito:ital,wght@0,300;0,400;0,600;0,800;1,400;1,600&display=swap">
<style>
  :root{
    --navy:#1f4360;
    --navy-deep:#173550;
    --tan:#c6a488;
    --tan-light:#d8bfa9;
    --ink:#1f3f5b;
    --paper:#ffffff;
    --stage:#dfdddf;
    --stage-dark:#0e0e0e;
    --brick:#a88f82;
    --brick-light:#cfc3bb;
    --sky:#e6e3e2;
    --haze:#9aa8ba;
  }
  *{box-sizing:border-box;margin:0;padding:0}
  html,body{width:1200px;height:2503px;overflow:hidden}
  body{position:relative;background:var(--paper);font-family:"Nunito",sans-serif;color:var(--ink)}

  .stage-top{position:absolute;left:0;top:0;width:1200px;height:710px;background:var(--stage)}
  .stage-band{position:absolute;left:0;top:710px;width:1200px;height:110px;background:var(--stage-dark)}
  .hero{position:absolute;left:161px;top:85px;width:878px;height:494px}

  .thumb{position:absolute;width:540px;height:304px;overflow:hidden}
  .thumb .slide{transform:scale(.615);transform-origin:0 0}
  .col-l{left:51px}.col-r{left:609px}
  .row-1{top:852px}.row-2{top:1174px}.row-3{top:1496px}.row-4{top:1817px}.row-5{top:2139px}

  /* slide base */
  .slide{position:relative;width:878px;height:494px;overflow:hidden;background:var(--paper)}
  .photo{position:absolute}
  .photo-street{inset:0;background:
      linear-gradient(180deg,var(--sky) 0%,var(--sky) 18%,transparent 40%),
      linear-gradient(90deg,#c9bfb8 0%,var(--brick) 45%,#8c7467 70%,#b3a296 100%);}
  .wash{position:absolute;inset:0}
  .wash-light{background:linear-gradient(90deg,rgba(255,255,255,.98) 0%,rgba(255,255,255,.9) 30%,rgba(255,255,255,.45) 65%,rgba(255,255,255,.15) 100%)}
  .wash-dark{background:linear-gradient(90deg,rgba(31,67,96,1) 0%,rgba(31,67,96,.92) 30%,rgba(31,67,96,.55) 65%,rgba(31,67,96,.35) 100%)}

  .brand{position:absolute;display:flex;align-items:center;gap:8px;font-weight:800;font-size:28px;color:var(--navy);letter-spacing:.5px}
  .brand .square{width:14px;height:14px;background:var(--tan)}
  .brand.on-dark{color:var(--paper)}
  .brand.small{font-size:15px;gap:5px}
  .brand.small .square{width:8px;height:8px}

  .title{position:absolute;left:86px;top:198px;font-weight:800;font-size:52px;line-height:56px;color:var(--navy)}
  .subtitle{position:absolute;left:86px;top:318px;font-weight:300;font-size:26px;color:var(--navy)}
  .date{position:absolute;left:86px;top:362px;font-size:12px;color:var(--navy)}
  .on-dark-text .title,.on-dark-text .subtitle,.on-dark-text .date{color:var(--paper)}

  .band{position:absolute;left:0;bottom:0;width:100%;height:36px;display:flex;align-items:center;justify-content:center;font-size:12px;color:var(--paper)}
  .band-gradient{background:linear-gradient(90deg,var(--navy) 0%,var(--navy) 30%,var(--tan) 100%)}
  .band-white{background:var(--paper);color:var(--ink)}
  .band-tan{background:var(--tan)}

  .copyright{position:absolute;right:34px;bottom:20px;display:flex;align-items:center;gap:8px;font-size:10px;color:var(--paper)}
  .page-no{width:16px;height:16px;background:var(--tan);display:flex;align-items:center;justify-content:center;font-size:9px;font-weight:800}

  /* tasks */
  .tasks-photo{left:546px;top:0;width:332px;height:494px;background:linear-gradient(180deg,#e4e2e0 0%,#d2c4bb 35%,#a2877a 60%,#6f7d92 100%)}
  .tasks-head{position:absolute;left:76px;top:58px;font-weight:800;font-size:28px;letter-spacing:1px;color:var(--navy)}
  .tasks-rule{position:absolute;left:78px;top:100px;width:78px;height:8px;border-radius:4px;background:linear-gradient(90deg,var(--tan),var(--tan-light))}
  .tasks-box{position:absolute;left:0;top:155px;width:720px;height:235px;background:linear-gradient(90deg,var(--navy) 0%,#3d5670 45%,#a48e7d 85%,var(--tan) 100%);display:flex;gap:28px;padding:22px 0 0 76px}
  .task-list{list-style:none;width:282px;color:var(--paper);font-style:italic;font-size:11px;line-height:12.5px}
  .task-list li{position:relative;padding-left:22px;margin-bottom:9px}
  .task-list li::before{content:"";position:absolute;left:2px;top:4px;width:4px;height:4px;border-radius:50%;background:var(--paper)}

  /* project */
  .project-bg{inset:0;background:linear-gradient(180deg,#c8ced8 0%,#aeb7c4 40%,#6e819b 80%,#4b6382 100%)}
  .project-card{position:absolute;left:16px;top:32px;width:325px;height:378px;border-radius:8px;background:rgba(238,238,240,.88);box-shadow:0 2px 10px rgba(0,0,0,.15);display:flex;flex-direction:column;align-items:center;padding-top:88px;text-align:center}
  .project-tag{position:absolute;left:0;top:36px;width:360px;height:44px;background:linear-gradient(90deg,var(--navy) 0%,#5a6b7c 45%,var(--tan) 100%);border-radius:0 6px 6px 0;color:var(--paper);font-weight:800;font-size:23px;letter-spacing:1.5px;padding-left:46px;display:flex;align-items:center}
  .icon{width:52px;height:52px;border-radius:50%;display:flex;align-items:center;justify-content:center}
  .icon-pin{background:var(--tan)}
  .icon-bulb{background:var(--navy);margin-top:14px}
  .site{margin-top:12px;font-weight:800;font-size:15px;line-height:17px;color:#222}
  .proposal{margin-top:8px;font-weight:600;font-size:16px;color:var(--tan)}
  .proposal-text{margin-top:10px;width:250px;font-style:italic;font-size:11px;line-height:12.5px;color:#333}
  .shot{position:absolute;border:2px solid var(--paper)}
  .shot-brick{background:linear-gradient(160deg,#8a6f62 0%,#a47e6b 50%,#5d4b43 100%)}
  .shot-garden{background:linear-gradient(180deg,#cdd3da 0%,#59703f 55%,#9a9b95 100%)}
  .shot-render{background:linear-gradient(180deg,#d9dce0 0%,#5b5652 45%,#b9b6b0 100%)}
  .shot-wall{background:linear-gradient(180deg,#8d9093 0%,#827669 60%,#6f6b67 100%)}
  .shot-drawing{background:linear-gradient(135deg,#fbfbf7 0%,#eef0ea 100%)}
  .shot-plan{background:linear-gradient(135deg,#fdfbe6 0%,#f2efcf 100%)}
  .brand-foot{left:30px;bottom:20px}

  /* contact */
  .contact-head{position:absolute;left:98px;top:220px;font-weight:800;font-size:16px;letter-spacing:1.5px;color:var(--paper)}
  .contact-address{position:absolute;left:98px;top:252px;width:300px;font-size:11.5px;line-height:13px;color:var(--paper)}
  .contact-list{position:absolute;left:98px;top:306px;list-style:none;color:var(--paper);font-size:11.5px}
  .contact-list li{display:flex;align-items:center;gap:12px;height:25px}
</style>
</head>
<body>

<div class="stage-top"></div>
<div class="stage-band"></div>

<!-- featured title slide -->
<div class="hero">
  <section class="slide">
    <div class="photo photo-street" role="img" aria-label="Street photograph of a brick corner building with shop front"></div>
    <div class="wash wash-light"></div>
    <div class="brand" style="left:86px;top:110px"><span class="square"></span>Brelvon</div>
    <h1 class="title">Brelvon Innovative<br>Design Solution</h1>
    <p class="subtitle">Project Portfolio</p>
    <p class="date">Tuesday, June 4, 2024</p>
    <footer class="band band-gradient">© 2024 Brelvon Innovative Design Solution. All rights reserved.</footer>
  </section>
</div>

<!-- title light -->
<div class="thumb col-l row-1">
  <section class="slide">
    <div class="photo photo-street" role="img" aria-label="Street photograph of a brick corner building with shop front"></div>
    <div class="wash wash-light"></div>
    <div class="brand" style="left:86px;top:110px"><span class="square"></span>Brelvon</div>
    <h1 class="title">Brelvon Innovative<br>Design Solution</h1>
    <p class="subtitle">Project Portfolio</p>
    <p class="date">Tuesday, June 4, 2024</p>
    <footer class="band band-gradient">© 2024 Brelvon Innovative Design Solution. All rights reserved.</footer>
  </section>
</div>

<!-- title dark -->
<div class="thumb col-r row-1">
  <section class="slide on-dark-text">
    <div class="photo photo-street" role="img" aria-label="Street photograph of a brick corner building with shop front"></div>
    <div class="wash wash-dark"></div>
    <div class="brand on-dark" style="left:86px;top:110px"><span class="square"></span>Brelvon</div>
    <h1 class="title">Brelvon Innovative<br>Design Solution</h1>
    <p class="subtitle">Project Portfolio</p>
    <p class="date">Tuesday, June 4, 2024</p>
    <footer class="band band-white">© 2024 Brelvon Innovative Design Solution. All rights reserved.</footer>
  </section>
</div>

<!-- tasks -->
<div class="thumb col-l row-2">
  <section class="slide">
    <div class="photo tasks-photo" role="img" aria-label="Blurred street photograph of brick buildings"></div>
    <h2 class="tasks-head">TASKS</h2>
    <div class="tasks-rule"></div>
    <div class="tasks-box">
      <ul class="task-list">
        <li>Creating working drawings</li>
        <li>Price breakdown of total build costs</li>
        <li>Liaising with Vale Water for water connection, drainage connection</li>
        <li>Liaising with Northway Gas to get gas supply to site</li>
        <li>Liaising with Grid Power Network to get electric supply</li>
        <li>Tendering out works to different tradesman</li>
        <li>Getting material orders</li>
      </ul>
      <ul class="task-list">
        <li>Arranging structural engineer for the site</li>
        <li>Arranging Building control for the site</li>
        <li>Making sure material is on site on time</li>
        <li>Making sure all tradesman work is up to current British standards</li>
        <li>Daily walk rounds to check work is done according to approved plans</li>
        <li>Placing orders for bathrooms, kitchen, and flooring</li>
        <li>All snag work with main contactor</li>
      </ul>
    </div>
    <div class="brand small" style="left:26px;top:440px"><span class="square"></span>Brelvon</div>
    <div class="copyright">© 2024 Brelvon Innovative Design Solution. All rights reserved.<span class="page-no">3</span></div>
  </section>
</div>

<!-- project 1 -->
<div class="thumb col-r row-2">
  <section class="slide">
    <div class="photo project-bg" role="img" aria-label="Blurred background photograph of the project site"></div>
    <div class="project-card">
      <div class="icon icon-pin"><svg width="22" height="28" viewBox="0 0 22 28"><path d="M11 1C5.5 1 1.5 5 1.5 10.3 1.5 17 11 27 11 27s9.5-10 9.5-16.7C20.5 5 16.5 1 11 1z" fill="none" stroke="#fff" stroke-width="2"/><circle cx="11" cy="10.5" r="3.5" fill="none" stroke="#fff" stroke-width="2"/></svg></div>
      <p class="site">Garages at Larkfield Mews,<br>Larkfield Street, Dunholt</p>
      <div class="icon icon-bulb"><svg width="22" height="28" viewBox="0 0 22 28"><path d="M11 2a8 8 0 0 0-5 14.2V20h10v-3.8A8 8 0 0 0 11 2z" fill="#fff"/><rect x="7" y="22" width="8" height="2" fill="#fff"/><rect x="8" y="25" width="6" height="2" fill="#fff"/></svg></div>
      <p class="proposal">Proposal</p>
      <p class="proposal-text">Change of use from garages to two dwelling houses (use class C3) including alterations to the front and side elevations</p>
    </div>
    <div class="project-tag">PROJECT #1</div>
    <div class="shot shot-brick" style="left:380px;top:41px;width:283px;height:144px" role="img" aria-label="Photograph of garages along a brick lane"></div>
    <div class="shot shot-plan" style="left:672px;top:41px;width:166px;height:144px" role="img" aria-label="Floor plan drawings of the proposed houses"></div>
    <div class="shot shot-brick" style="left:380px;top:194px;width:458px;height:235px" role="img" aria-label="Photograph of the converted brick houses"></div>
    <div class="brand small on-dark brand-foot"><span class="square"></span>Brelvon</div>
    <div class="copyright">© 2024 Brelvon Innovative Design Solution. All rights reserved.<span class="page-no">4</span></div>
  </section>
</div>

<!-- project 2 -->
<div class="thumb col-l row-3">
  <section class="slide">
    <div class="photo project-bg" role="img" aria-label="Blurred background photograph of the project site"></div>
    <div class="project-card">
      <div class="icon icon-pin"><svg width="22" height="28" viewBox="0 0 22 28"><path d="M11 1C5.5 1 1.5 5 1.5 10.3 1.5 17 11 27 11 27s9.5-10 9.5-16.7C20.5 5 16.5 1 11 1z" fill="none" stroke="#fff" stroke-width="2"/><circle cx="11" cy="10.5" r="3.5" fill="none" stroke="#fff" stroke-width="2"/></svg></div>
      <p class="site">118 Quarrell Road,<br>Dunholt</p>
      <div class="icon icon-bulb"><svg width="22" height="28" viewBox="0 0 22 28"><path d="M11 2a8 8 0 0 0-5 14.2V20h10v-3.8A8 8 0 0 0 11 2z" fill="#fff"/><rect x="7" y="22" width="8" height="2" fill="#fff"/><rect x="8" y="25" width="6" height="2" fill="#fff"/></svg></div>
      <p class="proposal">Proposal</p>
      <p class="proposal-text">Change of use from offices (use class B1) to 12 flats (use class C3)</p>
    </div>
    <div class="project-tag">PROJECT #2</div>
    <div class="shot shot-garden" style="left:382px;top:41px;width:224px;height:144px" role="img" aria-label="Photograph of the office building behind trees"></div>
    <div class="shot shot-brick" style="left:616px;top:41px;width:222px;height:144px" role="img" aria-label="Photograph of the building frontage and car park"></div>
    <div class="shot shot-drawing" style="left:382px;top:196px;width:456px;height:232px" role="img" aria-label="Floor plan and elevation drawings of the proposed flats"></div>
    <div class="brand small on-dark brand-foot"><span class="square"></span>Brelvon</div>
    <div class="copyright">© 2024 Brelvon Innovative Design Solution. All rights reserved.<span class="page-no">5</span></div>
  </section>
</div>

<!-- project 3 -->
<div class="thumb col-r row-3">
  <section class="slide">
    <div class="photo project-bg" role="img" aria-label="Blurred background photograph of the project site"></div>
    <div class="project-card">
      <div class="icon icon-pin"><svg width="22" height="28" viewBox="0 0 22 28"><path d="M11 1C5.5 1 1.5 5 1.5 10.3 1.5 17 11 27 11 27s9.5-10 9.5-16.7C20.5 5 16.5 1 11 1z" fill="none" stroke="#fff" stroke-width="2"/><circle cx="11" cy="10.5" r="3.5" fill="none" stroke="#fff" stroke-width="2"/></svg></div>
      <p class="site">61-65 Marlow Street,<br>Dunholt</p>
      <div class="icon icon-bulb"><svg width="22" height="28" viewBox="0 0 22 28"><path d="M11 2a8 8 0 0 0-5 14.2V20h10v-3.8A8 8 0 0 0 11 2z" fill="#fff"/><rect x="7" y="22" width="8" height="2" fill="#fff"/><rect x="8" y="25" width="6" height="2" fill="#fff"/></svg></div>
      <p class="proposal">Proposal</p>
      <p class="proposal-text">Refurbishment Of Commercial Ground Floor Units Together With Formation Of 6 Residential Units On First And Second Floors. Installation Of Glazing And Repair To External Masonry Including Bricking Up Of Existing Openings</p>
    </div>
    <div class="project-tag">PROJECT #3</div>
    <div class="shot shot-wall" style="left:380px;top:41px;width:222px;height:186px" role="img" aria-label="Photograph of the rendered gable end of the building"></div>
    <div class="shot shot-wall" style="left:613px;top:41px;width:225px;height:186px" role="img" aria-label="Photograph of the street terrace"></div>
    <div class="shot shot-plan" style="left:380px;top:238px;width:458px;height:190px" role="img" aria-label="Coloured floor plans of the ground, first and second floors"></div>
    <div class="brand small on-dark brand-foot"><span class="square"></span>Brelvon</div>
    <div class="copyright">© 2024 Brelvon Innovative Design Solution. All rights reserved.<span class="page-no">6</span></div>
  </section>
</div>

<!-- project 4 -->
<div class="thumb col-l row-4">
  <section class="slide">
    <div class="photo project-bg" role="img" aria-label="Blurred background photograph of the project site"></div>
    <div class="project-card">
      <div class="icon icon-pin"><svg width="22" height="28" viewBox="0 0 22 28"><path d="M11 1C5.5 1 1.5 5 1.5 10.3 1.5 17 11 27 11 27s9.5-10 9.5-16.7C20.5 5 16.5 1 11 1z" fill="none" stroke="#fff" stroke-width="2"/><circle cx="11" cy="10.5" r="3.5" fill="none" stroke="#fff" stroke-width="2"/></svg></div>
      <p class="site">Land At 2 Ashcombe Rise,<br>Dunholt&nbsp; DN12 3QT</p>
      <div class="icon icon-bulb"><svg width="22" height="28" viewBox="0 0 22 28"><path d="M11 2a8 8 0 0 0-5 14.2V20h10v-3.8A8 8 0 0 0 11 2z" fill="#fff"/><rect x="7" y="22" width="8" height="2" fill="#fff"/><rect x="8" y="25" width="6" height="2" fill="#fff"/></svg></div>
      <p class="proposal">Proposal</p>
      <p class="proposal-text">Erection of a dwelling house (use class C3)</p>
    </div>
    <div class="project-tag">PROJECT #4</div>
    <div class="shot shot-plan" style="left:382px;top:41px;width:224px;height:235px" role="img" aria-label="Floor plans and site plan of the new house"></div>
    <div class="shot shot-garden" style="left:616px;top:41px;width:222px;height:136px" role="img" aria-label="Photograph of the overgrown plot"></div>
    <div class="shot shot-drawing" style="left:382px;top:285px;width:224px;height:143px" role="img" aria-label="Proposed front elevation drawing"></div>
    <div class="shot shot-render" style="left:616px;top:186px;width:222px;height:242px" role="img" aria-label="Photograph of the completed brick house"></div>
    <div class="brand small on-dark brand-foot"><span class="square"></span>Brelvon</div>
    <div class="copyright">© 2024 Brelvon Innovative Design Solution. All rights reserved.<span class="page-no">7</span></div>
  </section>
</div>

<!-- project 5 -->
<div class="thumb col-r row-4">
  <section class="slide">
    <div class="photo project-bg" role="img" aria-label="Blurred background photograph of the project site"></div>
    <div class="project-card">
      <div class="icon icon-pin"><svg width="22" height="28" viewBox="0 0 22 28"><path d="M11 1C5.5 1 1.5 5 1.5 10.3 1.5 17 11 27 11 27s9.5-10 9.5-16.7C20.5 5 16.5 1 11 1z" fill="none" stroke="#fff" stroke-width="2"/><circle cx="11" cy="10.5" r="3.5" fill="none" stroke="#fff" stroke-width="2"/></svg></div>
      <p class="site">31, Fennick Street,<br>Harlbury</p>
      <div class="icon icon-bulb"><svg width="22" height="28" viewBox="0 0 22 28"><path d="M11 2a8 8 0 0 0-5 14.2V20h10v-3.8A8 8 0 0 0 11 2z" fill="#fff"/><rect x="7" y="22" width="8" height="2" fill="#fff"/><rect x="8" y="25" width="6" height="2" fill="#fff"/></svg></div>
      <p class="proposal">Proposal</p>
      <p class="proposal-text">Warehouse conversion to 4 town houses.</p>
    </div>
    <div class="project-tag">PROJECT #5</div>
    <div class="shot shot-brick" style="left:380px;top:41px;width:125px;height:141px" role="img" aria-label="Photograph of the warehouse facade"></div>
    <div class="shot shot-wall" style="left:518px;top:41px;width:131px;height:141px" role="img" aria-label="Photograph of the rear courtyard"></div>
    <div class="shot shot-drawing" style="left:660px;top:41px;width:178px;height:141px" role="img" aria-label="Floor plan drawings of the town houses"></div>
    <div class="shot shot-brick" style="left:380px;top:193px;width:458px;height:235px" role="img" aria-label="Photograph of the arched brick warehouse frontage"></div>
    <div class="brand small on-dark brand-foot"><span class="square"></span>Brelvon</div>
    <div class="copyright">© 2024 Brelvon Innovative Design Solution. All rights reserved.<span class="page-no">8</span></div>
  </section>
</div>

<!-- contact tan -->
<div class="thumb col-l row-5">
  <section class="slide">
    <div class="photo photo-street" role="img" aria-label="Street photograph of a brick corner building with shop front"></div>
    <div class="wash wash-dark"></div>
    <div class="brand on-dark" style="left:98px;top:110px"><span class="square"></span>Brelvon</div>
    <h2 class="contact-head">CONTACT US</h2>
    <p class="contact-address">Unit 4 Harrowfield Court, Eastmere,<br>Dunholt DN14 7QR</p>
    <ul class="contact-list">
      <li><svg width="14" height="14" viewBox="0 0 24 24"><path d="M6.6 10.8a15 15 0 0 0 6.6 6.6l2.2-2.2a1 1 0 0 1 1-.25 11.4 11.4 0 0 0 3.6.57 1 1 0 0 1 1 1V20a1 1 0 0 1-1 1A17 17 0 0 1 3 4a1 1 0 0 1 1-1h3.5a1 1 0 0 1 1 1c0 1.25.2 2.45.57 3.6a1 1 0 0 1-.25 1z" fill="#fff"/></svg>+447700900418</li>
      <li><svg width="14" height="14" viewBox="0 0 24 24"><circle cx="12" cy="12" r="4" fill="none" stroke="#fff" stroke-width="2.4"/><path d="M16 8v5a3 3 0 0 0 6 0v-1a10 10 0 1 0-4 8" fill="none" stroke="#fff" stroke-width="2.4"/></svg>info@brelvon.co.uk</li>
      <li><svg width="14" height="14" viewBox="0 0 24 24"><circle cx="12" cy="12" r="10" fill="none" stroke="#fff" stroke-width="2"/><path d="M2 12h20M12 2c3 3 3 17 0 20M12 2c-3 3-3 17 0 20" fill="none" stroke="#fff" stroke-width="1.6"/></svg>www.brelvon.co.uk</li>
    </ul>
    <footer class="band band-tan" style="color:var(--ink)">© 2024 Brelvon Innovative Design Solution. All rights reserved.</footer>
  </section>
</div>

<!-- contact white -->
<div class="thumb col-r row-5">
  <section class="slide">
    <div class="photo photo-street" role="img" aria-label="Street photograph of a brick corner building with shop front"></div>
    <div class="wash wash-dark"></div>
    <div class="brand on-dark" style="left:98px;top:110px"><span class="square"></span>Brelvon</div>
    <h2 class="contact-head">CONTACT US</h2>
    <p class="contact-address">Unit 4 Harrowfield Court, Eastmere,<br>Dunholt DN14 7QR</p>
    <ul class="contact-list">
      <li><svg width="14" height="14" viewBox="0 0 24 24"><path d="M6.6 10.8a15 15 0 0 0 6.6 6.6l2.2-2.2a1 1 0 0 1 1-.25 11.4 11.4 0 0 0 3.6.57 1 1 0 0 1 1 1V20a1 1 0 0 1-1 1A17 17 0 0 1 3 4a1 1 0 0 1 1-1h3.5a1 1 0 0 1 1 1c0 1.25.2 2.45.57 3.6a1 1 0 0 1-.25 1z" fill="#fff"/></svg>+447700900418</li>
      <li><svg width="14" height="14" viewBox="0 0 24 24"><circle cx="12" cy="12" r="4" fill="none" stroke="#fff" stroke-width="2.4"/><path d="M16 8v5a3 3 0 0 0 6 0v-1a10 10 0 1 0-4 8" fill="none" stroke="#fff" stroke-width="2.4"/></svg>info@brelvon.co.uk</li>
      <li><svg width="14" height="14" viewBox="0 0 24 24"><circle cx="12" cy="12" r="10" fill="none" stroke="#fff" stroke-width="2"/><path d="M2 12h20M12 2c3 3 3 17 0 20M12 2c-3 3-3 17 0 20" fill="none" stroke="#fff" stroke-width="1.6"/></svg>www.brelvon.co.uk</li>
    </ul>
    <footer class="band band-white">© 2024 Brelvon Innovative Design Solution. All rights reserved.</footer>
  </section>
</div>

</body>
</html>
```